Window Cleaning Flyer targeting Shopfronts and Small Commercial Work

Single page flyer similar to the flyer targeting small commercial work and shopfronts

Please include the following text:

Brisk Pane Services delivers high quality service to suburbs all around Melbourne. From Frankston to Kalkallo, Brisk has you covered!

With over 10 years experience, Brisk specialises in providing:
- Window Cleaning: via elevated work platforms, rope access and extension poles
- Pressure Cleaning: Including chlorine treatment to prevent mould regrowth on concrete area
- Roof Gutter Cleaning: using our ladder free gutter vacuum

We pride ourselves on neat and professional presentation and vast geographical reach across Melbourne.

Our services can be completed on a frequency that meets your window cleaning needs. Whether a weekly clean or a yearly service.

Brisk Pane Services Melbourne takes care of all your window cleaning needs.

Contact Us now for free quote!

Target Market(s)

Small business and commercial building owners

Industry/Entity Type

Window Cleaning

Requirements
Must have
• Only use photos/logos provided
Should not have
• Stock phots

```html
<!DOCTYPE html>
<html lang="en">
<head>
<meta charset="utf-8">
<title>Brisk Pane Services – Window Cleaning Flyer</title>
<link rel="stylesheet" href="https://fonts.googleapis.com/css2?family=Roboto:wght@400;500;700;900&display=swap">
<style>
  :root {
    --stage: #ecebe6;
    --yellow: #f4ec1c;
    --yellow-soft: #ece468;
    --yellow-deep: #d9d214;
    --black: #111111;
    --band: #1c1c1c;
    --white: #ffffff;
    --brand-blue: #0f5289;
    --photo-light: #bdbdbd;
    --photo-dark: #4a4a4a;
  }
  * { box-sizing: border-box; margin: 0; padding: 0; }
  html, body {
    width: 1200px; height: 2320px; overflow: hidden;
    background: var(--stage);
    font-family: "Roboto", Arial, sans-serif;
  }
  .flyer {
    position: absolute; left: 0; top: 310px;
    width: 1200px; height: 1700px; overflow: hidden;
  }
  .flyer-backdrop {
    position: absolute; inset: 0;
    background: radial-gradient(ellipse at 75% 10%, var(--yellow-soft), var(--yellow) 45%, var(--yellow-deep));
  }

  /* left info panel */
  .info-panel {
    position: absolute; left: 32px; top: 50px;
    width: 580px; height: 1370px;
    background: var(--black);
    transform: rotate(-3deg); transform-origin: top left;
    padding: 60px 40px 0 40px;
    color: var(--white);
  }
  .brand-box {
    width: 395px; height: 230px; margin: 0 auto;
    background: var(--brand-blue);
    display: flex; align-items: center; justify-content: center;
    text-align: center;
  }
  .brand-name {
    color: var(--yellow); font-weight: 900; font-size: 50px; line-height: 1.05;
    text-transform: uppercase;
  }
  .tagline {
    margin-top: 60px; text-align: center;
    font-size: 37px; font-weight: 500; line-height: 1.2;
  }
  .free-quote {
    margin-top: 60px; color: var(--yellow);
    font-size: 68px; font-weight: 900; letter-spacing: 0.5px;
  }
  .selling-point { margin-top: 52px; }
  .selling-point + .selling-point { margin-top: 62px; }
  .selling-point h3 {
    color: var(--yellow); font-size: 36px; font-weight: 700; line-height: 1.2;
  }
  .selling-point p {
    font-size: 28px; line-height: 1.28; font-weight: 400;
  }

  /* contact block */
  .contact {
    position: absolute; left: 70px; top: 1440px; width: 520px;
    transform: rotate(-3deg); transform-origin: top left;
    text-align: center; color: var(--black);
  }
  .contact-title { font-size: 44px; font-weight: 700; }
  .contact-phone { font-size: 60px; font-weight: 900; letter-spacing: 1px; line-height: 1.1; }
  .contact-web { font-size: 27px; font-weight: 500; margin-top: 6px; }

  /* service cards */
  .service-card {
    position: absolute; left: 648px; width: 526px; height: 490px;
    background: var(--white); padding: 6px;
    transform: rotate(-4deg); transform-origin: top left;
    box-shadow: 0 6px 14px rgba(0,0,0,0.18);
  }
  .service-card.window   { top: 72px; }
  .service-card.pressure { top: 604px; }
  .service-card.gutter   { top: 1136px; }
  .service-photo {
    position: absolute; left: 6px; right: 6px; top: 6px; bottom: 6px;
    background: linear-gradient(160deg, var(--photo-light), var(--photo-dark));
  }
  .service-title {
    position: absolute; left: 6px; right: 6px; bottom: 112px; height: 88px;
    background: rgba(20,20,20,0.92);
    color: var(--white); font-size: 40px; font-weight: 700;
    display: flex; align-items: center; justify-content: center;
    text-transform: uppercase; white-space: nowrap;
  }
  .service-caption {
    position: absolute; left: 6px; right: 6px; bottom: 6px; height: 106px;
    background: var(--yellow);
    color: var(--black); font-size: 24px; line-height: 1.25;
    display: flex; align-items: center; justify-content: center;
    text-align: center; padding: 0 36px;
  }
</style>
</head>
<body>
<main class="flyer">
  <div class="flyer-backdrop" role="img" aria-label="Yellow-toned photo of tree foliage behind the flyer content"></div>

  <section class="info-panel">
    <div class="brand-box">
      <span class="brand-name">Brisk Pane<br>Services</span>
    </div>
    <p class="tagline">Takes care of all your<br>Window Cleaning needs!</p>
    <p class="free-quote">FREE QUOTE!</p>

    <div class="selling-point">
      <h3>Delivers High Quality Service</h3>
      <p>To suburbs all around Melbourne.<br>From Frankston to Kalkallo.<br>Brisk has you covered!</p>
    </div>
    <div class="selling-point">
      <h3>10 years Experience</h3>
      <p>We pride ourselves on neat and professional presentation and vast geographical reach across Melbourne.</p>
    </div>
    <div class="selling-point">
      <h3>Weekly or Yearly Service</h3>
      <p>Our services can be completed on a frequency that meets your window cleaning needs. Whether a weekly clean or a yearly service.</p>
    </div>
  </section>

  <section class="contact">
    <p class="contact-title">Contact Us!</p>
    <p class="contact-phone">000-000-000-000</p>
    <p class="contact-web">www.briskpaneservices.com</p>
  </section>

  <article class="service-card window">
    <div class="service-photo" role="img" aria-label="Black and white photo of a worker cleaning windows of a building with a long extension pole"></div>
    <h2 class="service-title">Window Cleaning</h2>
    <p class="service-caption">Via elevated work platforms, rope access and extension poles.</p>
  </article>

  <article class="service-card pressure">
    <div class="service-photo" role="img" aria-label="Black and white photo of a worker on an elevated platform pressure cleaning a wall"></div>
    <h2 class="service-title">Pressure Cleaning</h2>
    <p class="service-caption">Including chlorine treatment to prevent mould regrowth on concrete area</p>
  </article>

  <article class="service-card gutter">
    <div class="service-photo" role="img" aria-label="Black and white photo of a worker cleaning roof gutters with a pole vacuum"></div>
    <h2 class="service-title">Roof Gutter Cleaning</h2>
    <p class="service-caption">Cleaning using our ladder free gutter vacuum</p>
  </article>
</main>
</body>
</html>
```